QRV Stationery Design Project

Dear Designers,
We need a new stationery design for company to match our new logo.
Designers should provide a design for the following:
1. Business Card: 3.5x2 Inches.
2. Letterhead: A4 size.
3. Envelops: 25x35.5 Cm.
You can keep the Arabic name at the bottom of the logo Or you can use the separate attached Arabic Name.
Please refer to the attached logo guide for design information.
Sample Business Card information:
Name: Tariq Nawaf
Position: Operation Manager
Tel: +966 920007714 Ex. 500
Fax: +966 (3)8842617
Mob: +966 (5)00387251
email: tariq@qrv-example.com.sa
URL: www.qrv-example.com.sa
Address:
Al Wadi Tower, Suite 303
Nasser bin Salem Str.
Khobar, 31847
Saudi Arabia
Updates
Dear All,
Please note, we had uploaded our logo along with Arabic writing in Adobe illustrator format (.ai).
Regards,
Khalid
Dear All,
A sample data for the business card had been added as per your request.
Regards,
Khalid

```html
<!DOCTYPE html>
<html lang="en">
<head>
<meta charset="utf-8">
<title>QRV Business Card</title>
<link href="https://fonts.googleapis.com/css2?family=Ubuntu:wght@400;500;700&display=swap" rel="stylesheet">
<style>
  :root {
    --navy: #0d3f63;
    --navy-dark: #0a3352;
    --ink: #1f2a33;
    --rule: #1d4a6d;
    --paper: #ffffff;
    --stage: #dfe4e8;
  }
  * { margin: 0; padding: 0; box-sizing: border-box; }
  html, body { width: 1200px; height: 960px; overflow: hidden; }
  body {
    background: var(--stage);
    font-family: "Ubuntu", sans-serif;
    color: var(--ink);
    position: relative;
  }
  .card {
    position: absolute;
    left: 285px;
    width: 630px;
    height: 360px;
    box-shadow: 0 6px 18px rgba(0,0,0,0.18);
  }
  .card-front { top: 90px; background: var(--paper); }
  .card-back { top: 510px; background: var(--navy); }

  .brand {
    position: absolute;
    display: flex;
    align-items: center;
    gap: 12px;
    font-weight: 700;
    letter-spacing: 2px;
  }
  .card-front .brand { top: 40px; right: 44px; font-size: 52px; color: var(--navy); }
  .card-front .brand-square { width: 34px; height: 34px; background: var(--navy); }
  .card-back .brand { top: 120px; left: 0; right: 0; justify-content: center; font-size: 84px; color: var(--paper); }
  .card-back .brand-square { width: 52px; height: 52px; background: var(--paper); }

  .holder { position: absolute; left: 40px; top: 162px; }
  .holder-name { font-size: 32px; font-weight: 400; line-height: 1.1; }
  .holder-title { font-size: 18px; font-weight: 400; margin-top: 6px; }

  .divider {
    position: absolute;
    left: 40px; right: 40px; top: 240px;
    height: 1.5px; background: var(--rule);
  }

  .contacts {
    position: absolute; left: 40px; top: 254px;
    list-style: none; font-size: 15px; line-height: 22px;
  }
  .contacts li { display: flex; align-items: center; gap: 12px; }
  .contacts svg { width: 14px; height: 14px; fill: var(--navy); flex: none; }

  .address {
    position: absolute; left: 384px; top: 254px;
    font-size: 13px; line-height: 19px; font-style: normal;
  }

  .website {
    position: absolute; left: 0; right: 0; bottom: 58px;
    text-align: center; color: var(--paper);
    font-size: 14px; font-weight: 700; letter-spacing: 1px;
  }
</style>
</head>
<body>

<section class="card card-front">
  <div class="brand"><span class="brand-square"></span><span class="brand-name">QRV</span></div>

  <div class="holder">
    <h1 class="holder-name">Tariq Nawaf</h1>
    <p class="holder-title">Operation Manager</p>
  </div>

  <div class="divider"></div>

  <ul class="contacts">
    <li>
      <svg viewBox="0 0 16 16"><path d="M3 1l3 3-1.5 2c1 2 3 4 5 5l2-1.5 3 3-2 2C6 14 2 10 1 3z"/></svg>
      +966 920007714 Ex. 500
    </li>
    <li>
      <svg viewBox="0 0 16 16"><path d="M4 1h8v4H4z M1 6h14v7h-3v2H4v-2H1z M5 10h6v4H5z" fill-rule="evenodd"/></svg>
      +966 (3)8842617
    </li>
    <li>
      <svg viewBox="0 0 16 16"><path d="M4 0h8v16H4z M5.5 2h5v7h-5z" fill-rule="evenodd"/></svg>
      +966 (5)00387251
    </li>
    <li>
      <svg viewBox="0 0 16 16"><path d="M1 6l7-5 7 5v9H1z M3 7l5 4 5-4v6H3z" fill-rule="evenodd"/></svg>
      tariq@qrv-example.com.sa
    </li>
  </ul>

  <address class="address">
    Al Wadi Tower, Suite 303<br>
    Nasser bin Salem Str.<br>
    Khobar, 31847<br>
    Saudi Arabia
  </address>
</section>

<section class="card card-back">
  <div class="brand"><span class="brand-square"></span><span class="brand-name">QRV</span></div>
  <p class="website">www.qrv-example.com.sa</p>
</section>

</body>
</html>
```